Ironvale Fight Circuit Mixed Martial Art Events webpage

We need a website built for our new mixed martial art combat event. It needs a place to display the fighters, the event and date, sponsors and a blog. We would also like to run some videos, sell some merchandise and we're thinking of a page to stream the event by live feed.
Updates

Target Market(s)

Fans of MMA (Mixed Martial Arts)

Industry/Entity Type

Events

Number of Pages Required

4 page

Font styles to use
Sans Serif

Colors
000000
fbee3f
ffffff

Requirements
Must have
• Must have a part for live twitter feed.
• A place to put updates.
• A place to discuss details of the event.
• A buy now button to purchase tickets through seatq88.

```html
<!DOCTYPE html>
<html lang="en">
<head>
<meta charset="utf-8">
<title>Blog – Ironvale Fight Circuit</title>
<link href="https://fonts.googleapis.com/css2?family=Montserrat:wght@400;600;700&family=Oswald:wght@500;700&display=swap" rel="stylesheet">
<style>
:root{
  --page:#0e0e0e;
  --header:#000000;
  --accent:#fbce0b;
  --white:#ffffff;
  --muted:#9a9a9a;
  --line:#2c2c2c;
  --outside:#ffffff;
}
*{margin:0;padding:0;box-sizing:border-box}
html,body{width:1200px;height:1200px;overflow:hidden;background:var(--outside)}
body{font-family:'Montserrat',sans-serif;color:var(--white)}
.site{position:absolute;left:401px;top:0;width:398px;height:1200px;background:var(--page);overflow:hidden}
.site-header{position:absolute;left:0;top:0;width:100%;height:30px;background:var(--header)}
.brand{position:absolute;left:37px;top:9px;font-weight:700;font-size:10px;color:var(--white);letter-spacing:.5px}
.main-nav{position:absolute;top:12px;left:0;width:100%;font-size:4px;font-weight:600;letter-spacing:.2px}
.main-nav span{position:absolute;white-space:nowrap}
.main-nav .active::after{content:"";position:absolute;left:0;right:0;top:7px;height:1px;background:var(--accent)}
.search-icon{position:absolute;left:346px;top:10px;width:9px;height:9px}
.page-title{position:absolute;left:0;top:30px;width:100%;height:65px;background:var(--accent);display:flex;align-items:center;justify-content:center;padding-top:11px}
.page-title h1{font-family:'Oswald',sans-serif;font-weight:500;font-size:12px;color:#111;letter-spacing:.3px}
.blog-search{position:absolute;left:27px;top:113px;width:82px;height:12px;border:1px solid #3a3a3a;font-size:3.5px;color:var(--muted);display:flex;align-items:center;padding-left:12px}
.blog-search svg{position:absolute;left:4px;top:3px;width:5px;height:5px}
.post{position:absolute;left:28px;width:335px;height:81px}
.post-photo{position:absolute;left:0;top:0;width:138px;height:81px}
.post-body{position:absolute;left:147px;top:11px;width:188px}
.post-title{font-size:4.6px;font-weight:700;letter-spacing:.1px}
.post:first-child .post-title{color:var(--accent)}
.post-date{font-size:2.8px;color:var(--muted);margin-top:1px}
.post-excerpt{font-size:3.6px;line-height:4.85px;text-align:justify;margin-top:6px;color:#e8e8e8}
.post-link{position:absolute;left:1px;top:57px;font-size:3.6px;font-weight:600;white-space:nowrap}
.pagination{position:absolute;top:1078px;left:0;width:100%;font-size:4px}
.pagination span{position:absolute}
.pagination .current{color:var(--accent)}
.footer-rule{position:absolute;left:28px;top:1109px;width:341px;height:1px;background:var(--line)}
.footer-brand{position:absolute;left:58px;top:1135px;font-weight:700;font-size:15px;color:#7a7a7a}
.copyright{position:absolute;left:58px;top:1157px;font-size:3.4px;line-height:4.2px;color:var(--muted)}
.footer-col{position:absolute;top:1124px;font-size:3.6px;color:var(--muted)}
.footer-col h4{font-size:4.4px;font-weight:600;color:#cfcfcf;letter-spacing:.3px;margin-bottom:5px}
.footer-col li{list-style:none;height:10.6px}
.social-dots{display:flex;gap:3px;margin-top:-4px;margin-bottom:5px}
.social-dots i{width:3px;height:3px;border-radius:50%;background:#cfcfcf;display:block}
</style>
</head>
<body>
<div class="site">
  <header class="site-header">
    <div class="brand">IFC</div>
    <nav class="main-nav">
      <span style="left:118px">HOME</span>
      <span style="left:146px">FIGHTERS</span>
      <span style="left:180px">UPCOMING EVENTS</span>
      <span class="active" style="left:236px">BLOG</span>
      <span style="left:262px">STREAM</span>
    </nav>
    <svg class="search-icon" viewBox="0 0 10 10"><circle cx="4" cy="4" r="3" fill="none" stroke="#fff" stroke-width="1.2"/><line x1="6.2" y1="6.2" x2="9" y2="9" stroke="#fff" stroke-width="1.2"/></svg>
  </header>

  <section class="page-title"><h1>BLOG</h1></section>

  <div class="blog-search">
    <svg viewBox="0 0 10 10"><circle cx="4" cy="4" r="3" fill="none" stroke="#9a9a9a" stroke-width="1.4"/><line x1="6.2" y1="6.2" x2="9" y2="9" stroke="#9a9a9a" stroke-width="1.4"/></svg>
    SEARCH BLOG
  </div>

  <main class="post-list">
    <article class="post" style="top:146px">
      <div class="post-photo" role="img" aria-label="Photo of two fighters and a referee in the cage after a bout" style="background:linear-gradient(120deg,#6b4434,#2a2a35 55%,#8a6a58)"></div>
      <div class="post-body"><h2 class="post-title">INIBUS BONORUM ET MALORUM</h2><p class="post-date">JANUARY 25, 2017</p><p class="post-excerpt">Sed ut perspiciatis unde omnis iste natus error sit voluptatem accusantium doloremque laudantium, totam rem aperiam, eaque ipsa quae ab illo inventore veritatis et quasi architecto beatae vitae dicta sunt explicabo. Nemo enim ipsam voluptatem quia voluptas sit aspernatur aut odit aut fugit, sed quia consequuntur magni dolores eos qui ratione voluptatem sequi nesciunt. Neque porro quisquam est, qui dolorem ipsum quia dolor sit amet, consectetur, adipisci velit, sed quia non numquam eius modi tempora incidunt ut labore et dolore magnam aliquam quaerat voluptatem. Nemo enim ipsam voluptatem...</p><a class="post-link" style="top:66px">READ FULL ARTICLE →</a></div>
    </article>
    <article class="post" style="top:237px">
      <div class="post-photo" role="img" aria-label="Photo of two fighters exchanging punches" style="background:linear-gradient(100deg,#3a2e2a,#9a6a52 45%,#5a3a30)"></div>
      <div class="post-body"><h2 class="post-title">INIBUS BONORUM ET MALORUM</h2><p class="post-date">JANUARY 25, 2017</p><p class="post-excerpt">Sed ut perspiciatis unde omnis iste natus error sit voluptatem accusantium doloremque laudantium, totam rem aperiam, eaque ipsa quae ab illo inventore veritatis et quasi architecto beatae vitae dicta sunt explicabo. Nemo enim ipsam voluptatem quia voluptas sit aspernatur aut odit aut fugit, sed quia consequuntur magni dolores eos qui ratione voluptatem sequi nesciunt. Neque porro quisquam est, qui dolorem ipsum quia dolor sit amet, consectetur, adipisci velit, sed quia non numquam eius modi tempora incidunt ut labore et dolore magnam aliquam quaerat voluptatem. Nemo enim ipsam voluptatem...</p><a class="post-link" style="top:66px">READ FULL ARTICLE →</a></div>
    </article>
    <article class="post" style="top:328px">
      <div class="post-photo" role="img" aria-label="Photo of a fighter landing a high kick" style="background:linear-gradient(110deg,#8a5e48,#2e2a2c 50%,#a07a66)"></div>
      <div class="post-body"><h2 class="post-title">INIBUS BONORUM ET MALORUM</h2><p class="post-date">JANUARY 25, 2017</p><p class="post-excerpt">Sed ut perspiciatis unde omnis iste natus error sit voluptatem accusantium doloremque laudantium, totam rem aperiam, eaque ipsa quae ab illo inventore veritatis et quasi architecto beatae vitae dicta sunt explicabo. Nemo enim ipsam voluptatem quia voluptas sit aspernatur aut odit aut fugit, sed quia consequuntur magni dolores eos qui ratione voluptatem sequi nesciunt. Neque porro quisquam est, qui dolorem ipsum quia dolor sit amet, consectetur, adipisci velit, sed quia non numquam eius modi tempora incidunt ut labore et dolore magnam aliquam quaerat voluptatem. Nemo enim ipsam voluptatem...</p><a class="post-link" style="top:66px">READ FULL ARTICLE →</a></div>
    </article>
    <article class="post" style="top:419px">
      <div class="post-photo" role="img" aria-label="Photo of a grappling exchange against the cage fence" style="background:linear-gradient(130deg,#1e1e22,#4a4448 45%,#9a7a5e 80%)"></div>
      <div class="post-body"><h2 class="post-title">INIBUS BONORUM ET MALORUM</h2><p class="post-date">JANUARY 25, 2017</p><p class="post-excerpt">Sed ut perspiciatis unde omnis iste natus error sit voluptatem accusantium doloremque laudantium, totam rem aperiam, eaque ipsa quae ab illo inventore veritatis et quasi architecto beatae vitae dicta sunt explicabo. Nemo enim ipsam voluptatem quia voluptas sit aspernatur aut odit aut fugit, sed quia consequuntur magni dolores eos qui ratione voluptatem sequi nesciunt. Neque porro quisquam est, qui dolorem ipsum quia dolor sit amet, consectetur, adipisci velit, sed quia non numquam eius modi tempora incidunt ut labore et dolore magnam aliquam quaerat voluptatem. Nemo enim ipsam voluptatem...</p><a class="post-link" style="top:66px">READ FULL ARTICLE →</a></div>
    </article>
    <article class="post" style="top:510px">
      <div class="post-photo" role="img" aria-label="Black and white event poster announcing a New York fight card" style="background:linear-gradient(180deg,#1a1a1a,#5a5a5a 50%,#151515)"></div>
      <div class="post-body"><h2 class="post-title">INIBUS BONORUM ET MALORUM</h2><p class="post-date">JANUARY 25, 2017</p><p class="post-excerpt">Sed ut perspiciatis unde omnis iste natus error sit voluptatem accusantium doloremque laudantium, totam rem aperiam, eaque ipsa quae ab illo inventore veritatis et quasi architecto beatae vitae dicta sunt explicabo. Nemo enim ipsam voluptatem quia voluptas sit aspernatur aut odit aut fugit, sed quia consequuntur magni dolores eos qui ratione voluptatem sequi nesciunt. Neque porro quisquam est, qui dolorem ipsum quia dolor sit amet, consectetur, adipisci velit, sed quia non numquam eius modi tempora incidunt ut labore et dolore magnam aliquam quaerat voluptatem. Nemo enim ipsam voluptatem...</p><a class="post-link" style="top:66px">READ FULL ARTICLE →</a></div>
    </article>
    <article class="post" style="top:601px">
      <div class="post-photo" role="img" aria-label="Photo of a fighter posing at the weigh-in stage" style="background:linear-gradient(100deg,#141418,#7a4a3c 50%,#8a1e22)"></div>
      <div class="post-body"><h2 class="post-title">INIBUS BONORUM ET MALORUM</h2><p class="post-date">JANUARY 25, 2017</p><p class="post-excerpt">Sed ut perspiciatis unde omnis iste natus error sit voluptatem accusantium doloremque laudantium, totam rem aperiam, eaque ipsa quae ab illo inventore veritatis et quasi architecto beatae vitae dicta sunt explicabo. Nemo enim ipsam voluptatem quia voluptas sit aspernatur aut odit aut fugit, sed quia consequuntur magni dolores eos qui ratione voluptatem sequi nesciunt. Neque porro quisquam est, qui dolorem ipsum quia dolor sit amet, consectetur, adipisci velit, sed quia non numquam eius modi tempora incidunt ut labore et dolore magnam aliquam quaerat voluptatem. Nemo enim ipsam voluptatem...</p><a class="post-link" style="top:66px">READ FULL ARTICLE →</a></div>
    </article>
    <article class="post" style="top:692px">
      <div class="post-photo" role="img" aria-label="Photo of two fighters facing off at a press event" style="background:linear-gradient(100deg,#5a4636,#a07e64 40%,#8a4a7a)"></div>
      <div class="post-body"><h2 class="post-title">INIBUS BONORUM ET MALORUM</h2><p class="post-date">JANUARY 25, 2017</p><p class="post-excerpt">Sed ut perspiciatis unde omnis iste natus error sit voluptatem accusantium doloremque laudantium, totam rem aperiam, eaque ipsa quae ab illo inventore veritatis et quasi architecto beatae vitae dicta sunt explicabo. Nemo enim ipsam voluptatem quia voluptas sit aspernatur aut odit aut fugit, sed quia consequuntur magni dolores eos qui ratione voluptatem sequi nesciunt. Neque porro quisquam est, qui dolorem ipsum quia dolor sit amet, consectetur, adipisci velit, sed quia non numquam eius modi tempora incidunt ut labore et dolore magnam aliquam quaerat voluptatem. Nemo enim ipsam voluptatem...</p><a class="post-link" style="top:66px">READ FULL ARTICLE →</a></div>
    </article>
    <article class="post" style="top:783px">
      <div class="post-photo" role="img" aria-label="Photo of a fighter flexing on the weigh-in stage" style="background:linear-gradient(110deg,#1a1a1c,#7a5a44 50%,#2a2a2c)"></div>
      <div class="post-body"><h2 class="post-title">INIBUS BONORUM ET MALORUM</h2><p class="post-date">JANUARY 25, 2017</p><p class="post-excerpt">Sed ut perspiciatis unde omnis iste natus error sit voluptatem accusantium doloremque laudantium, totam rem aperiam, eaque ipsa quae ab illo inventore veritatis et quasi architecto beatae vitae dicta sunt explicabo. Nemo enim ipsam voluptatem quia voluptas sit aspernatur aut odit aut fugit, sed quia consequuntur magni dolores eos qui ratione voluptatem sequi nesciunt. Neque porro quisquam est, qui dolorem ipsum quia dolor sit amet, consectetur, adipisci velit, sed quia non numquam eius modi tempora incidunt ut labore et dolore magnam aliquam quaerat voluptatem. Nemo enim ipsam voluptatem...</p><a class="post-link" style="top:66px">READ FULL ARTICLE →</a></div>
    </article>
    <article class="post" style="top:878px">
      <div class="post-photo" role="img" aria-label="Photo of a heated staredown separated by an official" style="background:linear-gradient(100deg,#22242e,#a0705a 45%,#b03a36 60%,#2a2a30)"></div>
      <div class="post-body"><h2 class="post-title">INIBUS BONORUM ET MALORUM</h2><p class="post-date">JANUARY 25, 2017</p><p class="post-excerpt">Sed ut perspiciatis unde omnis iste natus error sit voluptatem accusantium doloremque laudantium, totam rem aperiam, eaque ipsa quae ab illo inventore veritatis et quasi architecto beatae vitae dicta sunt explicabo. Nemo enim ipsam voluptatem quia voluptas sit aspernatur aut odit aut fugit, sed quia consequuntur magni dolores eos qui ratione voluptatem sequi nesciunt. Neque porro quisquam est, qui dolorem ipsum quia dolor sit amet, consectetur, adipisci velit, sed quia non numquam eius modi tempora incidunt ut labore et dolore magnam aliquam quaerat voluptatem. Nemo enim ipsam voluptatem...</p><a class="post-link" style="top:66px">READ FULL ARTICLE →</a></div>
    </article>
    <article class="post" style="top:970px">
      <div class="post-photo" role="img" aria-label="Photo of fighters squaring off at a weigh-in" style="background:linear-gradient(100deg,#6a4a40,#b08a74 35%,#3a3a40 60%,#6a4a3a)"></div>
      <div class="post-body"><h2 class="post-title">INIBUS BONORUM ET MALORUM</h2><p class="post-date">JANUARY 25, 2017</p><p class="post-excerpt">Sed ut perspiciatis unde omnis iste natus error sit voluptatem accusantium doloremque laudantium, totam rem aperiam, eaque ipsa quae ab illo inventore veritatis et quasi architecto beatae vitae dicta sunt explicabo. Nemo enim ipsam voluptatem quia voluptas sit aspernatur aut odit aut fugit, sed quia consequuntur magni dolores eos qui ratione voluptatem sequi nesciunt. Neque porro quisquam est, qui dolorem ipsum quia dolor sit amet, consectetur, adipisci velit, sed quia non numquam eius modi tempora incidunt ut labore et dolore magnam aliquam quaerat voluptatem. Nemo enim ipsam voluptatem...</p><a class="post-link" style="top:66px">READ FULL ARTICLE →</a></div>
    </article>
  </main>

  <nav class="pagination">
    <span class="current" style="left:160px">1</span>
    <span style="left:176px">2</span>
    <span style="left:191px">3</span>
    <span style="left:206px">4</span>
    <span style="left:221px">5</span>
    <span style="left:236px">6</span>
  </nav>

  <footer>
    <div class="footer-rule"></div>
    <div class="footer-brand">IFC</div>
    <p class="copyright">Copyright © 2017 IFC.<br>Ironvale Fight Circuit<br>All Rights Reserved.</p>
    <div class="footer-col" style="left:150px"><h4>SITEMAP</h4><ul><li>Home</li><li>About Us</li><li>Fighters</li><li>Upcoming Events</li><li>Blog</li></ul></div>
    <div class="footer-col" style="left:223px"><h4>FAQ</h4><ul><li>Schedule</li><li>Buy Tickets</li><li>Watch</li><li>Past Events</li></ul></div>
    <div class="footer-col" style="left:292px"><h4>CONNECT WITH US</h4><ul><li style="height:8px">Social</li><li style="height:10px"><div class="social-dots" style="margin-top:0"><i></i><i></i><i></i><i></i></div></li><li>Email</li><li>info@ironvale.com</li><li>careers@ironvale.com</li></ul></div>
  </footer>
</div>
</body>
</html>
```